FLOOR RENEWAL INSTITUTE
RUG REVIVAL INSTITUTE
Bright & Fun-filled
4817 Maplecrest Ln
Bakersfield, CA 93301
RUGREVIVALINSTITUTE@MAILORBIT.COM
RUGREVIVALINSTITUTE.COM

```html
<!DOCTYPE html>
<html lang="en">
<head>
<meta charset="utf-8">
<title>Rug Revival Institute — Stationery</title>
<link href="https://fonts.googleapis.com/css2?family=Open+Sans:wght@400;600;700&display=swap" rel="stylesheet">
<style>
  :root {
    --bg: #e6e6e6;
    --paper: #ffffff;
    --brand-blue: #1c5aa6;
    --band-grey: #9a9ea3;
    --text-grey: #8a8d91;
    --faint-blue: #e4ebf4;
    --shadow: rgba(0,0,0,0.18);
  }
  * { box-sizing: border-box; margin: 0; padding: 0; }
  html, body { width: 1200px; height: 778px; overflow: hidden; }
  body {
    background: var(--bg);
    font-family: "Open Sans", Arial, sans-serif;
    position: relative;
  }
  .sheet { position: absolute; background: var(--paper); box-shadow: 0 2px 8px var(--shadow); }

  .brand { display: flex; align-items: center; gap: 6px; color: var(--brand-blue); font-weight: 700; line-height: 1.05; }
  .brand-square { background: var(--brand-blue); flex: none; }
  .brand--light { color: #fff; }
  .brand--light .brand-square { background: #fff; }

  /* Letterhead */
  .letterhead { left: 139px; top: 55px; width: 461px; height: 624px; }
  .letterhead .brand { position: absolute; left: 34px; top: 36px; font-size: 17px; width: 210px; }
  .letterhead .brand-square { width: 28px; height: 28px; }
  .letterhead-watermark { position: absolute; left: 160px; top: 220px; width: 168px; height: 240px;
    background: radial-gradient(ellipse at center, var(--faint-blue) 0%, rgba(228,235,244,0.3) 70%, transparent 100%); }
  .letterhead-address { position: absolute; left: 0; right: 0; top: 568px; text-align: center; font-size: 11px; color: var(--text-grey); }
  .contact-band { position: absolute; left: 0; right: 0; bottom: 0; height: 31px; display: flex; font-size: 10.5px; color: #fff; }
  .contact-band span { display: flex; align-items: center; padding: 0 10px; }
  .band-web { background: var(--brand-blue); width: 160px; }
  .band-phone { background: var(--band-grey); width: 120px; justify-content: center; }
  .band-email { background: var(--brand-blue); flex: 1; justify-content: flex-end; font-size: 9px; }

  /* Business cards */
  .card { top: 60px; width: 216px; height: 115px; }
  .card-front { left: 624px; }
  .card-front .brand { position: absolute; left: 14px; top: 14px; font-size: 11px; width: 150px; }
  .card-front .brand-square { width: 20px; height: 20px; }
  .card-front .contact-band { height: 15px; font-size: 5.5px; }
  .card-front .band-web { width: 70px; padding: 0 5px; }
  .card-front .band-phone { width: 55px; padding: 0; }
  .card-front .band-email { padding: 0 5px; font-size: 4.8px; }
  .card-back { left: 852px; background: var(--brand-blue); color: #fff; }
  .card-back-address { position: absolute; left: 12px; top: 12px; font-size: 8px; line-height: 1.4; }
  .card-back-person { position: absolute; right: 12px; top: 12px; text-align: right; }
  .card-back-person .name { font-size: 9px; font-weight: 700; }
  .card-back-person .role { font-size: 5.5px; }
  .card-back .brand { position: absolute; left: 12px; bottom: 14px; font-size: 11px; width: 150px; }
  .card-back .brand-square { width: 20px; height: 20px; }

  /* Envelope */
  .envelope { left: 629px; top: 240px; width: 427px; height: 216px; }
  .envelope .brand { position: absolute; left: 14px; top: 22px; font-size: 11px; width: 150px; }
  .envelope .brand-square { width: 20px; height: 20px; }
  .envelope-band { position: absolute; left: 0; top: 185px; width: 175px; height: 14px; background: var(--brand-blue);
    color: #fff; font-size: 6.5px; display: flex; align-items: center; padding-left: 8px; }

  /* Large name mark */
  .name-mark { position: absolute; left: 760px; top: 680px; width: 250px; text-align: center;
    font-size: 19px; font-weight: 700; color: var(--text-grey); letter-spacing: 1px; }
</style>
</head>
<body>
  <section class="sheet letterhead">
    <div class="brand"><span class="brand-square"></span><span>RUG REVIVAL INSTITUTE</span></div>
    <div class="letterhead-watermark" role="img" aria-label="Faint illustration of a carpet cleaner at work"></div>
    <p class="letterhead-address">4817 Maplecrest Ln, Bakersfield, CA 93301</p>
    <div class="contact-band">
      <span class="band-web">rugrevivalinstitute.com</span>
      <span class="band-phone">(800) 555-0142</span>
      <span class="band-email">rugrevivalinstitute@mailorbit.com</span>
    </div>
  </section>

  <section class="sheet card card-front">
    <div class="brand"><span class="brand-square"></span><span>RUG REVIVAL INSTITUTE</span></div>
    <div class="contact-band">
      <span class="band-web">rugrevivalinstitute.com</span>
      <span class="band-phone">(800) 555-0142</span>
      <span class="band-email">rugrevivalinstitute@mailorbit.com</span>
    </div>
  </section>

  <section class="sheet card card-back">
    <p class="card-back-address">4817 Maplecrest Ln<br>Bakersfield, CA 93301</p>
    <div class="card-back-person">
      <p class="name">Dana Whitfield</p>
      <p class="role">Lead Instructor</p>
    </div>
    <div class="brand brand--light"><span class="brand-square"></span><span>RUG REVIVAL INSTITUTE</span></div>
  </section>

  <section class="sheet envelope">
    <div class="brand"><span class="brand-square"></span><span>RUG REVIVAL INSTITUTE</span></div>
    <div class="envelope-band">4817 Maplecrest Ln, Bakersfield, CA 93301</div>
  </section>

  <p class="name-mark">RUG REVIVAL INSTITUTE</p>
</body>
</html>
```